Wine Label Design

A wine label for 750ml bottles. Same label for different varieties with the variety / region / vintage to be updated as required.
Brand: Beyond the Ridge
Product Use: Front and Back label suitable for a 750 ml bottle (preferably Burgundy bottles)
Design Brief: Beyond the Ridge is a small winery that produces limited amounts of hand crafted wines that are aimed at the mid to top end of the market and requires a label befitting the work that goes into the creation of the wine. In terms of style i don't have any preconceptions and am open to a broad range of design suggestions at the same level of existing premium brands or innovative brands.
Must Have for Front label
Front Label
Beyond the Ridge
2013
Grampians
Shiraz
750ML (should be in smaller text)
Alc. 14% by Vol. (should be in smaller text)
Must Have for Back Label
Beyond the Ridge
2013
Grampians
Shiraz
www.beyondtheridge.com.au (should be in smaller text)
Product of Australia
Alc.14% by Vol. (should be in smaller text)
Contains preservative 220(should be in smaller text)
Below are some guides for dimensions:
The Front Label Size can be between
100 - 120 mm (Width) x 70 - 85 mm (Height)
The back label size can be between
90 mm (Width) x 70 - 85 mm (Height)
Updates
Target Market(s)
Medium to top end of the wine market who require the label to be a reflection of the wine.
Industry/Entity Type
Product
Colors
Designer to choose colors to be used in the design.
Look and feel
Each slider illustrates characteristics of the customer's brand and the style your logo design should communicate.

```html
<!DOCTYPE html>
<html lang="en">
<head>
<meta charset="utf-8">
<title>Beyond the Ridge – Grampians Shiraz 2013 Label</title>
<link href="https://fonts.googleapis.com/css2?family=Raleway:wght@300;400;500;700&display=swap" rel="stylesheet">
<style>
  :root {
    --paper: #ffffff;
    --ink: #1a1a1a;
    --ink-soft: #444444;
    --vine-green: #8cc49a;
    --vine-light: #cfe6cf;
    --sky-peach: #f6d9c4;
  }
  * { box-sizing: border-box; margin: 0; padding: 0; }
  html, body { width: 1200px; height: 510px; overflow: hidden; background: var(--paper); }
  body { font-family: "Raleway", sans-serif; color: var(--ink); }

  .label { position: relative; width: 1200px; height: 510px; background: var(--paper); }

  /* rotated columns read top to bottom */
  .turned { position: absolute; transform-origin: top left; transform: rotate(90deg); }

  .rule { position: absolute; background: var(--ink); }

  /* left regulatory strip */
  .legal { left: 84px; top: 75px; width: 240px; font-size: 10px; line-height: 14px; }
  .legal strong { display: block; font-weight: 700; letter-spacing: 0.2px; }
  .legal .fine { font-weight: 500; font-size: 9.5px; }
  .rule--legal { left: 88px; top: 75px; width: 2px; height: 316px; }
  .std-drinks { position: absolute; left: 12px; top: 346px; width: 72px; text-align: center; font-size: 8.5px; font-weight: 500; }
  .std-drinks svg { display: block; margin: 0 auto 3px; }

  /* front */
  .vineyard-art {
    position: absolute; left: 470px; top: 6px; width: 270px; height: 200px;
    background: linear-gradient(170deg, var(--sky-peach) 0%, var(--vine-light) 45%, var(--vine-green) 100%);
    border-radius: 40% 40% 30% 30% / 30% 30% 20% 20%;
    opacity: 0.85;
  }
  .variety {
    position: absolute; right: 675px; top: 188px; text-align: right;
    font-weight: 300; font-size: 44px; line-height: 58px; letter-spacing: -0.5px;
  }
  .rule--front { left: 540px; top: 195px; width: 2px; height: 170px; }
  .quote { position: absolute; left: 565px; top: 262px; font-size: 13px; line-height: 16px; color: var(--ink-soft); }
  .volume { position: absolute; left: 565px; top: 347px; font-size: 10.5px; font-weight: 500; }
  .brand-name {
    position: absolute; left: 0; width: 1060px; top: 428px; text-align: center;
    font-weight: 400; font-size: 50px; letter-spacing: 6px;
  }

  /* back */
  .rule--back { left: 990px; top: 75px; width: 2px; height: 316px; }
  .back-copy { left: 1174px; top: 75px; width: 316px; }
  .back-copy h2 { font-weight: 400; font-size: 22px; letter-spacing: 3px; line-height: 30px; }
  .back-copy h3 { font-weight: 300; font-size: 14px; line-height: 18px; margin-bottom: 6px; }
  .back-copy p { font-weight: 400; font-size: 9px; line-height: 12.5px; color: var(--ink-soft); text-align: justify; text-align-last: justify; margin-bottom: 3px; }
</style>
</head>
<body>
<div class="label">

  <div class="turned legal">
    <strong>www.beyondtheridge.com.au</strong>
    <strong>Product of Australia</strong>
    <span class="fine">750ml Alc.14% by Vol. Contains preservative 220</span>
  </div>
  <div class="rule rule--legal"></div>
  <div class="std-drinks">
    <svg width="34" height="30" viewBox="0 0 34 30" aria-hidden="true">
      <path d="M4 2 H30 L28 14 Q26 20 17 20 Q8 20 6 14 Z" fill="none" stroke="#1a1a1a" stroke-width="2"/>
      <line x1="17" y1="20" x2="17" y2="27" stroke="#1a1a1a" stroke-width="2"/>
      <line x1="10" y1="28" x2="24" y2="28" stroke="#1a1a1a" stroke-width="2"/>
      <text x="17" y="13" text-anchor="middle" font-family="Raleway, sans-serif" font-size="8" font-weight="700" fill="#1a1a1a">7.3</text>
    </svg>
    standard drinks
  </div>

  <div class="vineyard-art" role="img" aria-label="Watercolour sketch of rolling vineyard rows, a farmhouse with cypress trees and a fence"></div>
  <div class="variety">grampians<br>shiraz<br>2013</div>
  <div class="rule rule--front"></div>
  <p class="quote">"this could be a liitle<br>quote about the vineyard<br>or the wine"</p>
  <p class="volume">750ml&nbsp; Alc. 14% by Vol</p>
  <h1 class="brand-name">Beyond the Ridge</h1>

  <div class="rule rule--back"></div>
  <div class="turned back-copy">
    <h2>Beyond the Ridge</h2>
    <h3>grampians shiraz 2013</h3>
    <p>Beyond the Ridge is a boutique producer with select parcels of grapes selected from Victoria's premium wine growing regions.</p>
    <p>We pride ourselves on being involved with every step of the winemaking process and producing wines that are reflective of vintage location and wine making philosophy.</p>
    <p>We hope you enjoy our 2013 Grampians Shiraz</p>
  </div>

</div>
</body>
</html>
```